Website for a company focused on genealogical products and historical items

I need a website designed using our current branding.

Company name: R. L. Atelier: Merchants of Fine Heritage Prints

Our company sells ancestral art, downloadable worksheets pertaining to genealogy, and we offer weekend workshops and seminars.

the website should have the following pages:
landing page
products page: to include three different products: 1. a physical product with an intake form the customer completes online, 2. a downloadable product, and 3. a lecture/presentation booking page
about us page/history
contact page/sign up page

The website will include portraits of historical figures in gold frames, lots of white background, very clean design. We would like the website to feel fresh and clean, bright.

Target Market(s)

Older Americans interested in their family heritage and lineage

Industry/Entity Type

Genealogy, research, history, lectures

Coding

Coded - Design and coding required

Number of Pages Required

5+ page

Font styles to use
Serif
Other font styles liked:
• Libre Baskerville, Aliey, one historical script - P22 Royalist

Colors
0094D4
00A9DD
6FCCEA
C7EBF8
E9F6FB

Requirements
Must have
• must have our color branding and logo (pdf attached, and I can send original files), simple design, not too many images on each page (maybe one image per page)
Nice to have
• Nice to have clean design, all pages the same "look"
Should not have
• no black backgrounds, nothing too busy

```html
<!DOCTYPE html>
<html lang="en">
<head>
<meta charset="UTF-8">
<title>R. L. Atelier — Merchants of Fine Heritage Prints</title>
<link rel="stylesheet" href="https://fonts.googleapis.com/css2?family=Libre+Baskerville:wght@400;700&family=Outfit:wght@400;500;600;700&display=swap">
<style>
:root{
  --blue:#00A9DD;
  --blue-deep:#0094D4;
  --blue-soft:#6FCCEA;
  --blue-pale:#C7EBF8;
  --blue-mist:#EEF8FC;
  --footer-bg:#E6F6FB;
  --brown:#5A3A26;
  --ink:#1E1E1E;
  --text:#3A3A3A;
  --field:#EFEFEF;
  --white:#FFFFFF;
}
*{margin:0;padding:0;box-sizing:border-box}
html,body{width:1200px;height:3392px;overflow:hidden;background:var(--white)}
body{position:relative;font-family:"Libre Baskerville",serif;color:var(--text)}
.heading{font-family:"Outfit",sans-serif;font-weight:600;color:var(--blue)}
.abs{position:absolute}
a{text-decoration:none;color:inherit}

/* hero */
.hero{position:absolute;left:0;top:0;width:1200px;height:568px;
  background:radial-gradient(ellipse at 72% 20%,#e7a24c 0%,#a8622a 28%,#5e3419 60%,#2e1a10 100%)}
.hero-shade{position:absolute;inset:0;background:linear-gradient(90deg,rgba(30,18,10,.55) 0%,rgba(30,18,10,.15) 60%,rgba(30,18,10,0) 100%)}
.nav{position:absolute;left:141px;top:47px;width:918px;height:57px;background:var(--white);
  display:flex;align-items:center;padding:0 14px 0 28px;font-family:"Outfit",sans-serif;font-size:13px;font-weight:600;color:var(--ink)}
.nav a{margin-right:46px}
.nav a.active{color:var(--brown)}
.nav .contact-btn{margin-left:auto;margin-right:0;background:var(--brown);color:var(--white);padding:12px 22px}
.brand-badge{position:absolute;left:551px;top:14px;width:98px;height:124px;background:var(--white);border-radius:49px 49px 4px 4px;
  display:flex;align-items:center;justify-content:center;text-align:center;font-family:"Outfit",sans-serif;font-weight:700;font-size:14px;line-height:1.2;color:var(--brown)}
.hero h1{position:absolute;left:141px;top:210px;font-family:"Outfit",sans-serif;font-weight:700;font-size:47px;color:var(--white);letter-spacing:-.5px}
.hero h2{position:absolute;left:141px;top:278px;font-family:"Outfit",sans-serif;font-weight:600;font-size:21px;color:var(--white)}
.hero p{position:absolute;left:141px;top:326px;width:470px;font-size:14px;line-height:23px;color:#f4ebe2}
.hero .btn{position:absolute;left:141px;top:423px;width:176px;height:38px;background:var(--white);color:var(--brown);
  font-family:"Outfit",sans-serif;font-weight:600;font-size:13px;display:flex;align-items:center;justify-content:center}

/* buttons */
.pill{background:var(--blue);color:var(--white);border-radius:20px;font-family:"Outfit",sans-serif;font-weight:600;font-size:12.5px;display:flex;align-items:center;justify-content:center}
.pill.abs{position:absolute}

/* text columns */
.text-col{position:absolute}
.text-col h3{font-size:29px;line-height:1.2}
.text-col p{font-size:10.9px;line-height:20.5px}
.text-col p + p{margin-top:14px}
.text-col .pill{margin-top:26px;height:38px}

/* story */
.story-art{position:absolute;left:136px;top:628px}
.story .text-col{left:587px;top:642px;width:474px}
.story .text-col p:first-of-type{margin-top:26px}

/* legacy */
.legacy{position:absolute;left:0;top:1142px;width:1200px;height:511px;background:var(--blue-mist)}
.legacy h3{position:absolute;left:0;width:1200px;top:52px;text-align:center;font-size:29px}
.card{position:absolute;top:129px;width:213px}
.card .art{width:213px;height:263px;border-radius:4px}
.card h4{margin-top:20px;font-family:"Outfit",sans-serif;font-weight:600;font-size:14.5px;color:var(--ink)}
.card .link{display:inline-flex;align-items:center;gap:8px;margin-top:12px;font-size:13px;color:var(--blue);text-decoration:underline}

/* lectures */
.lectures .text-col{left:141px;top:1792px;width:432px}
.lectures .text-col p{margin-top:26px}

/* cta */
.cta{position:absolute;left:141px;top:2193px;width:918px;height:250px;background:var(--blue);border-radius:30px;text-align:center;color:var(--white)}
.cta h3{margin-top:44px;font-family:"Outfit",sans-serif;font-weight:600;font-size:29px}
.cta p{width:640px;margin:22px auto 0;font-size:11.2px;line-height:20.5px}
.cta .btn{position:absolute;left:357px;top:178px;width:205px;height:38px;background:var(--white);color:var(--blue);border-radius:20px;
  font-family:"Outfit",sans-serif;font-weight:600;font-size:12.5px;display:flex;align-items:center;justify-content:center}

/* contact */
.contact-art{position:absolute;left:141px;top:2529px;width:395px;height:421px;border-radius:20px;
  background:linear-gradient(180deg,#8a8a7e 0%,#6b5d48 35%,#3f3324 70%,#1f1a14 100%)}
.info{position:absolute;left:183px;color:var(--white);font-size:14.5px;line-height:22px}
.info .label{font-family:"Outfit",sans-serif;font-weight:600;font-size:14.5px}
.info svg{position:absolute;left:0;top:3px}
.info .body{margin-left:28px}
.contact h3{position:absolute;left:610px;top:2548px;font-size:29px}
.field{position:absolute;background:var(--field);border-radius:4px;font-size:13px;color:#777;padding:12px 14px}

/* footer */
.footer{position:absolute;left:0;top:3036px;width:1200px;height:356px;background:var(--footer-bg)}
.footer .brand{position:absolute;left:141px;top:96px;font-family:"Outfit",sans-serif;font-weight:700;font-size:22px;color:var(--brown);line-height:1.15}
.footer .brand .dot{display:block;width:60px;height:60px;border-radius:50%;background:var(--blue-pale);margin-bottom:12px}
.col{position:absolute;top:66px}
.col h5{font-family:"Outfit",sans-serif;font-weight:600;font-size:14px;color:var(--blue);margin-bottom:16px}
.col a{display:block;font-size:13.5px;color:var(--ink);line-height:27.5px}
.newsletter{position:absolute;left:773px;top:98px;width:285px;height:43px;background:var(--white);border-radius:6px;box-shadow:0 2px 6px rgba(0,120,170,.12);
  font-size:12px;color:#666;padding:14px 18px}
.newsletter .send{position:absolute;right:6px;top:7px;width:38px;height:29px;background:var(--blue);border-radius:5px;display:flex;align-items:center;justify-content:center}
.rule{position:absolute;left:141px;top:296px;width:918px;height:1px;background:#b9cfd8}
.copy{position:absolute;left:141px;top:318px;font-size:12px;color:var(--ink)}
.social{position:absolute;top:310px;width:30px;height:30px;border-radius:50%;background:var(--blue)}
</style>
</head>
<body>

<header class="hero">
  <div class="hero-shade" role="img" aria-label="Sunset scene of an ancient amphitheatre with crowds gathered below"></div>
  <nav class="nav">
    <a class="active">Home</a><a>Products</a><a>About Us</a>
    <a class="contact-btn">Contact Us</a>
  </nav>
  <div class="brand-badge">R. L.<br>Atelier</div>
  <h1>R. L. Atelier</h1>
  <h2>Merchants of Fine Heritage Prints</h2>
  <p>Step into the tapestry of history with Ancestral Art, where each masterpiece whispers the stories of our heritage through brushstrokes preserved across centuries.</p>
  <a class="btn">Explore Our Collections</a>
</header>

<section class="story">
  <svg class="story-art" width="386" height="432" viewBox="0 0 386 432">
    <defs>
      <linearGradient id="temple" x1="0" y1="0" x2="0" y2="1">
        <stop offset="0" stop-color="#8fa79c"/>
        <stop offset=".45" stop-color="#6b5a3e"/>
        <stop offset=".75" stop-color="#4f6b52"/>
        <stop offset="1" stop-color="#5d9a97"/>
      </linearGradient>
    </defs>
    <path d="M381 18 V260 Q381 330 300 380 L196 428 L110 390 Q20 345 14 300" fill="none" stroke="var(--blue)" stroke-width="2.5"/>
    <path d="M5 6 H374 V250 Q374 320 290 365 L188 415 L88 370 Q5 325 5 250 Z" fill="url(#temple)" role="img" aria-label="Painting of a classical temple beside a waterfall in a green gorge"/>
  </svg>
  <div class="text-col">
    <h3 class="heading">Our Story</h3>
    <p>It is a long established fact that a reader will be distracted by the readable content of a page when looking at its layout. The point of using Lorem Ipsum is that it has a more-or-less normal distribution of letters, as opposed to using 'Content here, content here', making it look like readable English. Many desktop publishing packages and web page editors now use Lorem Ipsum as their default model text, and a search for 'lorem ipsum' will uncover many web sites still in their infancy.</p>
    <p>There are many variations of passages of Lorem Ipsum available, but the majority have suffered alteration in some form, by injected humour, or randomised words which don't look even slightly believable.</p>
    <a class="pill" style="width:110px">Learn More</a>
  </div>
</section>

<section class="legacy">
  <h3 class="heading">Discover Your Legacy</h3>
  <div class="card" style="left:141px">
    <div class="art" role="img" aria-label="Painting of a domed basilica by a canal with gondolas" style="background:linear-gradient(160deg,#7fa3a0,#c9a05a 55%,#8a3b2a)"></div>
    <h4>Donec Pede Justo</h4><a class="link">View Product <svg width="14" height="8" viewBox="0 0 14 8"><path d="M0 4H12M9 1L12 4L9 7" stroke="currentColor" fill="none" stroke-width="1.3"/></svg></a>
  </div>
  <div class="card" style="left:375px">
    <div class="art" role="img" aria-label="Engraving of a classical column over a city avenue" style="background:linear-gradient(170deg,#d8cfbd,#a89b82 60%,#6f6656)"></div>
    <h4>Neoclassical Portrait</h4><a class="link">View Product <svg width="14" height="8" viewBox="0 0 14 8"><path d="M0 4H12M9 1L12 4L9 7" stroke="currentColor" fill="none" stroke-width="1.3"/></svg></a>
  </div>
  <div class="card" style="left:610px">
    <div class="art" role="img" aria-label="Ornate painted palace scene with horses and riders" style="background:linear-gradient(170deg,#d9c6a4,#b2523a 55%,#5a3a26)"></div>
    <h4>Gnome Busting Apparatus</h4><a class="link">View Product <svg width="14" height="8" viewBox="0 0 14 8"><path d="M0 4H12M9 1L12 4L9 7" stroke="currentColor" fill="none" stroke-width="1.3"/></svg></a>
  </div>
  <div class="card" style="left:844px">
    <div class="art" role="img" aria-label="Sepia illustration of two robed scholars reading a scroll" style="background:linear-gradient(170deg,#efe2cf,#b88a5e 55%,#6e4a30)"></div>
    <h4>The Energy Of Life</h4><a class="link">View Product <svg width="14" height="8" viewBox="0 0 14 8"><path d="M0 4H12M9 1L12 4L9 7" stroke="currentColor" fill="none" stroke-width="1.3"/></svg></a>
  </div>
</section>

<section class="lectures">
  <div class="text-col">
    <h3 class="heading">Lectures &amp; Seminars</h3>
    <p>There are many variations of passages of Lorem Ipsum available, but the majority have suffered alteration in some form, by injected humour, or randomised words which don't look even slightly believable. If you are going to use a passage of Lorem Ipsum, you need to be sure there isn't anything embarrassing hidden in the middle of text. All the Lorem Ipsum generators on the Internet tend to repeat predefined chunks as necessary, making this the first true generator on the Internet.</p>
    <a class="pill" style="width:132px">Book Seminar</a>
  </div>
  <svg class="abs" style="left:690px;top:1730px" width="360" height="385" viewBox="0 0 360 385">
    <defs>
      <linearGradient id="courtyard" x1="0" y1="0" x2="0" y2="1">
        <stop offset="0" stop-color="#b99a76"/>
        <stop offset=".5" stop-color="#9a5a3c"/>
        <stop offset="1" stop-color="#6e5a46"/>
      </linearGradient>
    </defs>
    <rect x="122" y="12" width="233" height="370" rx="116" fill="none" stroke="var(--blue)" stroke-width="1.8"/>
    <rect x="71" y="8" width="243" height="365" rx="121" fill="url(#courtyard)" role="img" aria-label="Painting of a crowded palace courtyard festival"/>
    <path d="M32 58 L37 73 L52 78 L37 83 L32 98 L27 83 L12 78 L27 73 Z" fill="var(--blue-soft)"/>
    <path d="M337 236 L341 249 L354 253 L341 257 L337 270 L333 257 L320 253 L333 249 Z" fill="var(--blue-soft)"/>
  </svg>
</section>

<section class="cta">
  <h3>Embrace Your Ancestral Journey</h3>
  <p>There are many variations of passages of Lorem Ipsum available, but the majority have suffered alteration in some form, by injected humour, or randomised words which don't look even slightly believable.</p>
  <a class="btn">Explore Products &amp; Services</a>
</section>

<section class="contact">
  <div class="contact-art" role="img" aria-label="Painting of an ancient amphitheatre with a crowd at dusk"></div>
  <div class="info" style="top:2734px">
    <svg width="18" height="18" viewBox="0 0 18 18"><path d="M9 1C6 1 4 3.2 4 6c0 3.5 5 9 5 9s5-5.5 5-9c0-2.8-2-5-5-5z" fill="none" stroke="#fff" stroke-width="1.6"/><circle cx="9" cy="6" r="1.8" fill="#fff"/><path d="M3 16h12" stroke="#fff" stroke-width="1.4"/></svg>
    <div class="body">123 Lorem ipsum dummy,<br>#567 Dummy road 1234</div>
  </div>
  <div class="info" style="top:2797px">
    <svg width="18" height="16" viewBox="0 0 18 16"><rect x="1" y="2" width="16" height="12" rx="1.5" fill="#fff"/><path d="M1.5 3L9 9L16.5 3" stroke="#3a2f22" stroke-width="1.4" fill="none"/></svg>
    <div class="body"><span class="label">Email</span><br>hello@rlatelier-prints.com</div>
  </div>
  <div class="info" style="top:2860px">
    <svg width="17" height="17" viewBox="0 0 17 17"><path d="M3.5 1.5l3 .5 1 3.5-2 1.5c1 2 2.5 3.5 4.5 4.5l1.5-2 3.5 1 .5 3c-1 1.5-2.5 2-4 1.5C7 14 3 10 1.8 5.5 1.4 4 2 2.5 3.5 1.5z" fill="#fff"/></svg>
    <div class="body"><span class="label">Phone</span><br>555-014-2290</div>
  </div>

  <h3 class="heading">Contact Us</h3>
  <div class="field" style="left:610px;top:2626px;width:217px;height:41px">First name</div>
  <div class="field" style="left:842px;top:2626px;width:216px;height:41px">Last name</div>
  <div class="field" style="left:610px;top:2683px;width:217px;height:41px">Phone</div>
  <div class="field" style="left:842px;top:2683px;width:216px;height:41px">Email</div>
  <div class="field" style="left:610px;top:2739px;width:448px;height:132px">Message</div>
  <a class="pill abs" style="left:610px;top:2900px;width:118px;height:38px">Submit Now</a>
</section>

<footer class="footer">
  <div class="brand"><span class="dot"></span>R. L.<br>Atelier</div>
  <div class="col" style="left:378px"><h5>Quick Links</h5><a>Home</a><a>Products</a><a>About Us</a></div>
  <div class="col" style="left:560px"><h5>Resources</h5><a>Privacy Policy</a><a>Terms Of Service</a></div>
  <div class="col" style="left:773px"><h5>Newsletter</h5></div>
  <div class="newsletter">Enter Your Email
    <span class="send"><svg width="16" height="16" viewBox="0 0 16 16"><path d="M15 1L1 7l5 2 2 5z" fill="#fff"/><path d="M15 1L6 9" stroke="var(--blue)" stroke-width="1.2"/></svg></span>
  </div>
  <div class="rule"></div>
  <div class="copy">© 2024 &nbsp;RLAtelier. All rights reserved.</div>
  <span class="social" style="left:908px"></span>
  <span class="social" style="left:948px"></span>
  <span class="social" style="left:988px"></span>
  <span class="social" style="left:1028px"></span>
</footer>

</body>
</html>
```